Brindle construction ltd staionary design
Project: Stationary
Stationary - Construction
Stationary
Professional
Directors Dan Brindle / Mark Brindle
BRINDLE CONSTRUCTION (GLOUCESTER) LTD
14 wexcombe road Gloucester GL4 8RQ
Brindleconstructionltd@fernmail.example
www.brindleconstructionlimited.example
would like stationary pack designed: business card, letterhead, envelope ect. Also a site sign please. Business card i would like black background to contrast my green logo with the logo in middle and details underneath. Letterhead i will leave to designer to come up with options. On site sign can i have logo ontop as main feature and underneath contact info with services incl ( New Builds, Extensions, Conversions, Refurbishments, Groundworks, Block Paving.) In logo attached use main logo ontop.
Main logo and underneath building contractor & Block paving specialist

```html
<!DOCTYPE html>
<html lang="en">
<head>
<meta charset="utf-8">
<title>Brindle Construction Ltd – Business Card</title>
<link rel="stylesheet" href="https://fonts.googleapis.com/css2?family=Arimo:wght@400;700&display=swap">
<style>
  :root {
    --page-bg: #e6e6e4;
    --card-black: #0a0a0a;
    --card-black-soft: #1a1a1a;
    --brand-green: #3fae2a;
    --brand-green-dark: #0f4d10;
    --brand-green-bright: #5fd23c;
    --swoosh-grey: #9a9a9a;
    --divider-grey: #5a5a5a;
    --text-white: #f2f2f2;
  }
  * { margin: 0; padding: 0; box-sizing: border-box; }
  html, body {
    width: 1200px;
    height: 780px;
    overflow: hidden;
    background: var(--page-bg);
    font-family: "Arimo", Arial, sans-serif;
  }
  .canvas {
    position: relative;
    width: 1200px;
    height: 780px;
  }
  .business-card {
    position: absolute;
    left: 80px;
    top: 100px;
    width: 1040px;
    height: 580px;
    border-radius: 36px;
    overflow: hidden;
    background: radial-gradient(ellipse at 60% 35%, var(--card-black-soft), var(--card-black) 70%);
    box-shadow: 0 10px 30px rgba(0,0,0,0.25);
  }
  .card-swoosh {
    position: absolute;
    inset: 0;
    width: 100%;
    height: 100%;
  }
  .company-name {
    position: absolute;
    left: 140px;
    top: 318px;
    width: 380px;
    color: var(--brand-green);
    font-weight: 700;
    font-size: 32px;
    letter-spacing: 1px;
    text-transform: uppercase;
    text-align: center;
    line-height: 1.15;
  }
  .company-name .name-main {
    display: block;
    font-size: 32px;
  }
  .divider {
    position: absolute;
    left: 540px;
    top: 80px;
    width: 2px;
    height: 430px;
    background: var(--divider-grey);
  }
  .contact-block {
    position: absolute;
    left: 574px;
    top: 98px;
    width: 440px;
    color: var(--text-white);
    font-size: 21px;
    line-height: 1.3;
  }
  .contact-name {
    color: var(--brand-green);
    font-size: 24px;
    margin-bottom: 56px;
  }
  .contact-address { margin-bottom: 58px; }
  .contact-row {
    display: flex;
    align-items: center;
    gap: 12px;
    height: 30px;
    white-space: nowrap;
  }
  .contact-icon {
    width: 20px;
    height: 22px;
    flex: none;
  }
  .contact-email { font-size: 17px; }
</style>
</head>
<body>
<main class="canvas">
  <section class="business-card" aria-label="Brindle Construction Ltd business card">
    <svg class="card-swoosh" viewBox="0 0 1040 580" preserveAspectRatio="none" aria-hidden="true">
      <defs>
        <linearGradient id="swooshGreen" x1="0" y1="0" x2="1" y2="1">
          <stop offset="0" stop-color="#0f4d10"/>
          <stop offset="0.55" stop-color="#3fae2a"/>
          <stop offset="1" stop-color="#5fd23c"/>
        </linearGradient>
      </defs>
      <path d="M0,70 C40,290 150,470 330,580 L0,580 Z" fill="url(#swooshGreen)"/>
      <path d="M20,40 C70,280 200,470 400,580" fill="none" stroke="#9a9a9a" stroke-width="7"/>
    </svg>

    <div class="company-name"><span class="name-main">Brindle</span>construction ltd</div>

    <div class="divider"></div>

    <div class="contact-block">
      <p class="contact-name">Mark Brindle</p>
      <p class="contact-address">14 wexcombe road<br>Gloucester, GL4 8RQ</p>
      <div class="contact-row">
        <svg class="contact-icon" viewBox="0 0 20 22" aria-hidden="true">
          <path d="M5 2 L8 2 L9 7 L7 8.5 C8 11.5 10 14 13 15 L14.5 13 L19 14 L19 18 C19 19 18 20 17 20 C9 19 2 12 2 4 C2 3 3 2 5 2 Z" fill="#3fae2a"/>
        </svg>
        <span>01452 730215</span>
      </div>
      <div class="contact-row">
        <svg class="contact-icon" viewBox="0 0 20 22" aria-hidden="true">
          <rect x="5" y="1" width="10" height="20" rx="2" fill="#3fae2a"/>
          <rect x="7" y="4" width="6" height="11" fill="#0a0a0a"/>
          <circle cx="10" cy="18" r="1.3" fill="#0a0a0a"/>
        </svg>
        <span>07700900418</span>
      </div>
      <div class="contact-row">
        <svg class="contact-icon" viewBox="0 0 20 22" aria-hidden="true">
          <rect x="1" y="5" width="18" height="12" rx="1.5" fill="#3fae2a"/>
          <path d="M2 6 L10 12 L18 6" fill="none" stroke="#0a0a0a" stroke-width="1.6"/>
        </svg>
        <span class="contact-email">Brindleconstructionltd@fernmail.example</span>
      </div>
    </div>
  </section>
</main>
</body>
</html>
```